The Coral Clinic PowerPoint Design

We are looking for a new PowerPoint template design to reflect our branding and to be used for presentations at international conferences and online conferences. An example of our current template which is outdated is attached. We would like to still have a blue colour background as this represents water (but the exact background can be modified). We would like a professional, modern, and sharp feel to the templates. The template should include an Intro Slide, content slide, and closing/questions slide. The template needs to be prepared for both the standards, the 4:3 and Wide screen 16:9. Logos and branding in the attached power point can be used. Please visit our website www.thecoralclinic.example to see more about the company.

```html
<!DOCTYPE html>
<html lang="en">
<head>
<meta charset="utf-8">
<title>The Coral Clinic – Presentation Template</title>
<link href="https://fonts.googleapis.com/css2?family=Baloo+2:wght@700&family=Montserrat:wght@400;600;700&display=swap" rel="stylesheet">
<style>
:root{
  --page:#eeeff1;
  --sea-top:#2ba0ec;
  --sea-mid:#1263c4;
  --sea-deep:#081a52;
  --yellow:#f3ea1c;
  --white:#ffffff;
  --button:#2f8fe6;
  --glass:rgba(200,214,232,.45);
  --tile:#7d9cc6;
  --green:#7cc243;
  --track:rgba(255,255,255,.35);
}
*{margin:0;padding:0;box-sizing:border-box}
html,body{width:1200px;height:2492px;overflow:hidden;background:var(--page)}
body{position:relative;font-family:"Montserrat",sans-serif;color:var(--white)}
.slide{position:absolute;width:545px;height:305px;overflow:hidden;
  background:linear-gradient(180deg,var(--sea-top) 0%,var(--sea-mid) 45%,var(--sea-deep) 100%);
  box-shadow:0 8px 18px rgba(0,0,0,.28)}
.slide.dark{background:linear-gradient(180deg,#1c74d4 0%,#0b3a8c 45%,#050e2c 100%)}
.col-a{left:35px}.col-b{left:620px}
.abs{position:absolute}
.heading{position:absolute;font-family:"Baloo 2",sans-serif;font-weight:700;color:var(--yellow);font-size:20px;line-height:1;top:14px;left:38px}
.heading::after{content:"";position:absolute;left:0;top:28px;width:22px;height:2px;background:var(--yellow)}
.heading.center{left:0;right:0;text-align:center}
.heading.center::after{left:50%;margin-left:-11px}
.body-text{position:absolute;font-size:7px;line-height:14.2px;text-align:justify}
.btn{position:absolute;background:var(--button);color:var(--white);font-size:6.5px;font-weight:600;border-radius:3px;text-align:center;line-height:18px;width:44px;height:18px;box-shadow:0 2px 4px rgba(0,0,0,.3)}
.badge{position:absolute;left:0;bottom:0;width:91px;height:30px;background:var(--green)}
.footer-note{position:absolute;bottom:8px;left:0;right:0;text-align:center;font-size:6px;line-height:8px}
.brand{position:absolute;display:flex;align-items:center;gap:4px;font-size:8.5px;font-weight:700;color:var(--white);white-space:nowrap}
.brand::before{content:"";width:7px;height:7px;border-radius:50%;background:var(--white)}
.brand.br{right:22px;bottom:12px}
.photo{position:absolute}
.ring{position:absolute;border-radius:50%;border:5px solid rgba(160,185,220,.55)}
.bullets{position:absolute;list-style:none;font-size:6px;line-height:8px}
.bullets li{position:relative;padding-left:9px;margin-bottom:31px;width:140px}
.bullets li::before{content:"";position:absolute;left:0;top:2px;width:3px;height:3px;border-radius:50%;background:var(--white)}
.laptop-screen{position:absolute;border:5px solid #111;border-radius:6px 6px 0 0;background:#000}
.laptop-base{position:absolute;height:7px;border-radius:0 0 10px 10px;background:linear-gradient(180deg,#e8eaee,#9aa0a8)}
</style>
</head>
<body>

<!-- Row 1 -->
<section class="slide dark col-a" style="top:39px">
  <div class="abs" style="top:13px;left:0;right:0;text-align:center;font-size:6px;letter-spacing:3px">WWW.THECORALCLINIC.EXAMPLE</div>
  <div class="abs" style="top:33px;left:252px;display:flex;gap:3px">
    <span style="width:12px;height:12px;border:1px solid #fff;border-radius:50%"></span>
    <span style="width:12px;height:12px;border:1px solid #fff;border-radius:50%"></span>
    <span style="width:12px;height:12px;border:1px solid #fff;border-radius:50%"></span>
  </div>
  <h1 class="abs" style="top:113px;left:0;right:0;text-align:center;font-family:'Baloo 2',sans-serif;font-size:21px;line-height:28px;color:var(--yellow)">THE CORAL CLINIC PRESENTATION<br>TEMPLATE</h1>
  <div class="abs" style="top:176px;left:207px;width:136px;height:14px;border-radius:7px;background:#fff;color:#0b3a8c;font-size:7px;font-weight:700;text-align:center;line-height:14px">PRESENTER NAME</div>
  <div class="abs" style="top:234px;left:0;right:0;text-align:center;font-size:6.5px">July, 2020</div>
  <div class="brand" style="top:272px;left:225px">The Coral Clinic</div>
</section>

<section class="slide col-b" style="top:39px">
  <h2 class="heading">Agenda</h2>
  <ul class="abs" style="top:75px;left:110px;list-style:none;font-size:8px;line-height:19.8px">
    <li><span style="color:var(--yellow)">•</span>&nbsp;&nbsp; Introduction</li>
    <li><span style="color:var(--yellow)">•</span>&nbsp;&nbsp; About Us</li>
    <li><span style="color:var(--yellow)">•</span>&nbsp;&nbsp; Welcome Massage</li>
    <li><span style="color:var(--yellow)">•</span>&nbsp;&nbsp; Our vision</li>
    <li><span style="color:var(--yellow)">•</span>&nbsp;&nbsp; Our Services</li>
    <li><span style="color:var(--yellow)">•</span>&nbsp;&nbsp; Portfolio</li>
    <li><span style="color:var(--yellow)">•</span>&nbsp;&nbsp; Team</li>
    <li><span style="color:var(--yellow)">•</span>&nbsp;&nbsp; Info graphic Charts</li>
    <li><span style="color:var(--yellow)">•</span>&nbsp;&nbsp; Contact Us</li>
  </ul>
  <div class="photo" role="img" aria-label="Photo of a sea turtle swimming in turquoise water" style="left:358px;top:49px;width:187px;height:213px;border-radius:18px 0 0 18px;background:linear-gradient(160deg,#3fb5d8,#1a8fb8 55%,#5cc6d6)"></div>
  <div class="abs" style="left:292px;top:212px;width:134px;height:30px;border-radius:5px;background:var(--button);font-size:8.5px;text-align:center;line-height:30px;box-shadow:0 2px 6px rgba(0,0,0,.3)">THE CORAL CLINIC</div>
  <div class="badge"></div>
  <div class="brand br">The Coral Clinic</div>
</section>

<!-- Row 2 -->
<section class="slide col-a" style="top:390px">
  <h2 class="heading">Introduction</h2>
  <p class="body-text" style="left:37px;top:92px;width:234px">Lorem ipsum dolor sit amet, consectetuer adipiscing elit, sed diam nonummy nibh euismod tincidunt ut laoreet dolore magna aliquam erat volutpat. Ut wisi enim ad minim veniam, quis nostrud exerci tation ullamcorper suscipit lobortis nisl ut aliquip ex ea commodo consequat. Duis autem vel eum iriure dolor in hendrerit in vulputate velit esse molestie consequat, vel illum dolore eu feugiat nulla facilisis at vero eros et accumsan et iusto odio dignissim qui blandit praesent luptatum zzril delenit augue duis dolore te feugait nulla facilisi.</p>
  <div class="abs" style="left:332px;top:50px;width:160px;height:202px;border-radius:18px;background:var(--glass)"></div>
  <svg class="abs" style="left:295px;top:55px" width="60" height="190" viewBox="0 0 60 190">
    <polygon points="30,2 54,16 54,42 30,56 6,42 6,16" fill="#f6a81c" stroke="#fff" stroke-width="2"/>
    <polygon points="30,66 54,80 54,106 30,120 6,106 6,80" fill="#1b9ab0" stroke="#fff" stroke-width="2"/>
    <polygon points="30,130 54,144 54,170 30,184 6,170 6,144" fill="#4cb848" stroke="#fff" stroke-width="2"/>
    <circle cx="30" cy="29" r="9" fill="none" stroke="#fff" stroke-width="1.5"/>
    <path d="M24 99 q3-12 6-12 q3 0 6 12 a6 6 0 0 1-12 0z" fill="none" stroke="#fff" stroke-width="1.5"/>
    <path d="M21 163 l9-16 9 16z" fill="none" stroke="#fff" stroke-width="1.5"/>
  </svg>
  <div class="abs" style="left:368px;top:88px;font-size:7px;line-height:8px">LOREM IPSUM DOLOR</div>
  <div class="abs" style="left:369px;top:147px;font-size:7px;line-height:8px">LOREM IPSUM DOLOR</div>
  <div class="abs" style="left:368px;top:210px;font-size:7px;line-height:8px">LOREM IPSUM DOLOR</div>
  <div class="badge"></div>
  <div class="footer-note">Home of the reef-keeper course<br>www.thecoralclinic.example</div>
  <div class="brand br">The Coral Clinic</div>
</section>

<section class="slide col-b" style="top:390px">
  <h2 class="heading center">Our Categories</h2>
  <div class="ring" style="left:35px;top:77px;width:92px;height:92px"></div>
  <div class="photo" role="img" aria-label="Photo of a penguin swimming underwater" style="left:42px;top:84px;width:78px;height:78px;border-radius:50%;background:linear-gradient(180deg,#4aa9c9,#2fb5b0)"></div>
  <div class="ring" style="left:162px;top:77px;width:92px;height:92px"></div>
  <div class="photo" role="img" aria-label="Photo of a seahorse" style="left:169px;top:84px;width:78px;height:78px;border-radius:50%;background:radial-gradient(circle,#c98a3c,#5a4a52)"></div>
  <div class="ring" style="left:289px;top:77px;width:92px;height:92px"></div>
  <div class="photo" role="img" aria-label="Photo of a tropical reef fish" style="left:296px;top:84px;width:78px;height:78px;border-radius:50%;background:radial-gradient(circle,#4fa8c4,#1f5f8a)"></div>
  <div class="ring" style="left:416px;top:77px;width:92px;height:92px"></div>
  <div class="photo" role="img" aria-label="Photo of an orange jellyfish" style="left:423px;top:84px;width:78px;height:78px;border-radius:50%;background:radial-gradient(circle,#f07a1c 20%,#1a3ec0 70%)"></div>
  <div class="abs" style="left:0;top:190px;width:545px;font-size:8px;font-weight:700">
    <span class="abs" style="left:36px;width:92px;text-align:center">CONSULTATION</span>
    <span class="abs" style="left:163px;width:92px;text-align:center">EDUCATION</span>
    <span class="abs" style="left:290px;width:92px;text-align:center">CONFERENCES</span>
    <span class="abs" style="left:417px;width:92px;text-align:center">REPRODUCTION</span>
  </div>
  <div class="btn" style="left:59px;top:210px">MORE</div>
  <div class="btn" style="left:186px;top:210px">MORE</div>
  <div class="btn" style="left:313px;top:210px">MORE</div>
  <div class="btn" style="left:440px;top:210px">MORE</div>
  <div class="brand" style="left:226px;top:270px">The Coral Clinic</div>
</section>

<!-- Row 3 -->
<section class="slide col-a" style="top:742px">
  <h2 class="heading">Welcome</h2>
  <div class="photo" role="img" aria-label="Illustration of a magnifying glass over a photo of a swimming penguin" style="left:0;top:62px;width:255px;height:213px;background:radial-gradient(ellipse at 63% 42%,rgba(190,205,225,.55),rgba(120,160,210,.25) 45%,rgba(40,100,190,0) 72%)"></div>
  <div class="abs" style="left:277px;top:59px;font-size:9.5px">CONSULTATION</div>
  <p class="body-text" style="left:277px;top:82px;width:215px">Lorem ipsum dolor sit amet, consectetuer adipiscing elit, sed diam nonummy nibh euismod tincidunt ut laoreet dolore magna aliquam erat volutpat. Ut wisi enim ad minim veniam, quis nostrud exerci tation ullamcorper suscipit lobortis nisl ut aliquip ex ea commodo consequat. Duis autem vel eum iriure dolor in vulputate velit esse molestie consequat, vel illum dolore eu feugiat nulla facilisis.</p>
  <div class="btn" style="left:279px;top:209px">MORE</div>
  <div class="badge"></div>
  <div class="footer-note">Home of the reef-keeper course<br>www.thecoralclinic.example</div>
  <div class="brand br">The Coral Clinic</div>
</section>

<section class="slide col-b" style="top:742px">
  <h2 class="heading">Our Services</h2>
  <div class="abs" style="left:0;top:0;width:545px;height:305px;font-size:5.5px;line-height:7.5px">
    <div class="abs" style="left:43px;top:72px;width:35px;height:35px;background:var(--tile);font-size:11px;font-weight:700;text-align:center;line-height:35px">1</div>
    <div class="abs" style="left:87px;top:72px;width:175px"><b style="letter-spacing:1px">TEXT INFORMATION</b><br><br>Lorem ipsum dolor sit amet, consectetuer adipiscing elit, sed diam nonummy nibh euismod tincidunt ut laoreet dolore magn</div>
    <div class="abs" style="left:43px;top:134px;width:35px;height:35px;background:var(--tile);font-size:11px;font-weight:700;text-align:center;line-height:35px">2</div>
    <div class="abs" style="left:87px;top:134px;width:175px"><b style="letter-spacing:1px">TEXT INFORMATION</b><br><br>Lorem ipsum dolor sit amet, consectetuer adipiscing elit, sed diam nonummy nibh euismod tincidunt ut laoreet dolore magn</div>
    <div class="abs" style="left:43px;top:196px;width:35px;height:35px;background:var(--tile);font-size:11px;font-weight:700;text-align:center;line-height:35px">3</div>
    <div class="abs" style="left:87px;top:196px;width:175px"><b style="letter-spacing:1px">TEXT INFORMATION</b><br><br>Lorem ipsum dolor sit amet, consectetuer adipiscing elit, sed diam nonummy nibh euismod tincidunt ut laoreet dolore magn</div>
    <div class="abs" style="left:295px;top:72px;width:35px;height:35px;background:var(--tile);font-size:11px;font-weight:700;text-align:center;line-height:35px">4</div>
    <div class="abs" style="left:339px;top:72px;width:175px"><b style="letter-spacing:1px">TEXT INFORMATION</b><br><br>Lorem ipsum dolor sit amet, consectetuer adipiscing elit, sed diam nonummy nibh euismod tincidunt ut laoreet dolore magn</div>
    <div class="abs" style="left:295px;top:134px;width:35px;height:35px;background:var(--tile);font-size:11px;font-weight:700;text-align:center;line-height:35px">5</div>
    <div class="abs" style="left:339px;top:134px;width:175px"><b style="letter-spacing:1px">TEXT INFORMATION</b><br><br>Lorem ipsum dolor sit amet, consectetuer adipiscing elit, sed diam nonummy nibh euismod tincidunt ut laoreet dolore magn</div>
    <div class="abs" style="left:295px;top:196px;width:35px;height:35px;background:var(--tile);font-size:11px;font-weight:700;text-align:center;line-height:35px">6</div>
    <div class="abs" style="left:339px;top:196px;width:175px"><b style="letter-spacing:1px">TEXT INFORMATION</b><br><br>Lorem ipsum dolor sit amet, consectetuer adipiscing elit, sed diam nonummy nibh euismod tincidunt ut laoreet dolore magn</div>
  </div>
  <div class="badge"></div>
  <div class="footer-note">Home of the reef-keeper course<br>www.thecoralclinic.example</div>
  <div class="brand br">The Coral Clinic</div>
</section>

<!-- Row 4 -->
<section class="slide col-a" style="top:1094px">
  <h2 class="heading">Vision</h2>
  <div class="abs" style="left:49px;top:87px;width:132px;height:153px;border-radius:14px;background:var(--glass)"></div>
  <div class="abs" style="left:210px;top:87px;width:132px;height:153px;border-radius:14px;background:var(--glass)"></div>
  <div class="abs" style="left:371px;top:87px;width:132px;height:153px;border-radius:14px;background:var(--glass)"></div>
  <svg class="abs" style="left:0;top:58px" width="545" height="60" viewBox="0 0 545 60">
    <polygon points="115,2 140,16 140,42 115,56 90,42 90,16" fill="#f6b41c" stroke="#fff" stroke-width="2"/>
    <polygon points="276,2 301,16 301,42 276,56 251,42 251,16" fill="#4cb848" stroke="#fff" stroke-width="2"/>
    <polygon points="437,2 462,16 462,42 437,56 412,42 412,16" fill="#1b9ab0" stroke="#fff" stroke-width="2"/>
    <ellipse cx="115" cy="29" rx="10" ry="6" fill="none" stroke="#fff" stroke-width="1.5"/><circle cx="115" cy="29" r="3" fill="#fff"/>
    <circle cx="276" cy="29" r="10" fill="none" stroke="#fff" stroke-width="1.5"/><circle cx="276" cy="29" r="5" fill="none" stroke="#fff" stroke-width="1.5"/>
    <circle cx="437" cy="29" r="10" fill="none" stroke="#fff" stroke-width="1.5"/><path d="M437 16v26M424 29h26" stroke="#fff" stroke-width="1.5"/>
  </svg>
  <div class="abs" style="left:49px;top:128px;width:132px;text-align:center">
    <div style="font-size:10px;font-weight:700">Vision</div>
    <p style="font-size:6px;line-height:9.6px;margin:8px 18px 0">Lorem ipsum dolor sit amet, consectetuer adipiscing elit, sed diam nonummy nibh euismod tincidunt ut laoreet dolore magna aliquam erat volutpat.</p>
  </div>
  <div class="abs" style="left:210px;top:130px;width:132px;text-align:center">
    <div style="font-size:10px;font-weight:700">Mission</div>
    <p style="font-size:6px;line-height:9.6px;margin:8px 18px 0">Lorem ipsum dolor sit amet, consectetuer adipiscing elit, sed diam nonummy nibh euismod tincidunt ut laoreet dolore magna aliquam erat volutpat.</p>
  </div>
  <div class="abs" style="left:371px;top:128px;width:132px;text-align:center">
    <div style="font-size:10px;font-weight:700">Goal</div>
    <p style="font-size:6px;line-height:9.6px;margin:8px 18px 0">Lorem ipsum dolor sit amet, consectetuer adipiscing elit, sed diam nonummy nibh euismod tincidunt ut laoreet dolore magna aliquam erat volutpat.</p>
  </div>
  <div class="badge"></div>
  <div class="footer-note">Home of the reef-keeper course<br>www.thecoralclinic.example</div>
  <div class="brand br">The Coral Clinic</div>
</section>

<section class="slide col-b" style="top:1094px">
  <h2 class="heading center">Infographic &amp; Mockup</h2>
  <div class="laptop-screen" style="left:75px;top:82px;width:191px;height:125px"></div>
  <div class="photo" role="img" aria-label="Screen photo of a hammerhead shark in dark teal water" style="left:80px;top:87px;width:181px;height:120px;background:radial-gradient(circle at 50% 45%,#1e6f78,#062a33)"></div>
  <div class="abs" style="left:80px;top:180px;width:181px;text-align:center;font-size:6px;line-height:8px">Add your text/ picture here and<br>send it to back</div>
  <div class="laptop-base" style="left:53px;top:207px;width:235px"></div>
  <ul class="bullets" style="left:333px;top:85px">
    <li>Lorem Ipsum is simply dummy text of the printing and typesetting industry.</li>
    <li>Lorem Ipsum is simply dummy text of the printing and typesetting industry.</li>
    <li>Lorem Ipsum is simply dummy text of the printing and typesetting industry.</li>
    <li>Lorem Ipsum is simply dummy text of the printing and typesetting industry.</li>
  </ul>
  <div class="brand" style="left:226px;top:270px">The Coral Clinic</div>
</section>

<!-- Row 5 -->
<section class="slide col-a" style="top:1446px">
  <h2 class="heading">Infographic</h2>
  <svg class="abs" style="left:33px;top:64px" width="86" height="186" viewBox="0 0 86 186">
    <circle cx="43" cy="43" r="40" fill="#e6eef6"/>
    <circle cx="43" cy="43" r="31" fill="none" stroke="#37b6d2" stroke-width="18" stroke-dasharray="142.4 194.8" transform="rotate(-90 43 43)"/>
    <circle cx="43" cy="43" r="40" fill="none" stroke="#8aa6c8" stroke-width="3"/>
    <circle cx="43" cy="138" r="40" fill="#e6eef6"/>
    <circle cx="43" cy="138" r="31" fill="none" stroke="#4d9be6" stroke-width="18" stroke-dasharray="97.4 194.8" transform="rotate(-90 43 138)"/>
    <circle cx="43" cy="138" r="40" fill="none" stroke="#8aa6c8" stroke-width="3"/>
  </svg>
  <div class="abs" style="left:33px;top:96px;width:86px;text-align:center;font-size:16px;font-weight:700;color:#0d3b7a">73%</div>
  <div class="abs" style="left:33px;top:191px;width:86px;text-align:center;font-size:16px;font-weight:700;color:#0d3b7a">50%</div>
  <div class="abs" style="left:131px;top:82px;width:110px;font-size:6px;line-height:12px"><b style="font-size:8px">PROJECT 01</b><br>Lorem Ipsum is simply dummy text of the printing and typesetting industry</div>
  <div class="abs" style="left:131px;top:177px;width:110px;font-size:6px;line-height:12px"><b style="font-size:8px">PROJECT 02</b><br>Lorem Ipsum is simply dummy text of the printing and typesetting industry</div>
  <div class="abs" style="left:268px;top:70px;width:229px;font-size:7.5px;font-weight:700">
    <div style="display:flex;justify-content:space-between"><span>PROJECT 03</span><span style="font-weight:400">32%</span></div>
    <div style="height:6px;margin:5px 0 19px;border-radius:3px;background:var(--track)"><div style="width:32%;height:6px;border-radius:3px;background:#c8d9ee"></div></div>
    <div style="display:flex;justify-content:space-between"><span>PROJECT 04</span><span style="font-weight:400">72%</span></div>
    <div style="height:6px;margin:5px 0 19px;border-radius:3px;background:var(--track)"><div style="width:72%;height:6px;border-radius:3px;background:#c8d9ee"></div></div>
    <div style="display:flex;justify-content:space-between"><span>PROJECT 05</span><span style="font-weight:400">52%</span></div>
    <div style="height:6px;margin:5px 0 19px;border-radius:3px;background:var(--track)"><div style="width:52%;height:6px;border-radius:3px;background:#c8d9ee"></div></div>
    <div style="display:flex;justify-content:space-between"><span>PROJECT 06</span><span style="font-weight:400">12%</span></div>
    <div style="height:6px;margin:5px 0 19px;border-radius:3px;background:var(--track)"><div style="width:18%;height:6px;border-radius:3px;background:#c8d9ee"></div></div>
    <div style="display:flex;justify-content:space-between"><span>PROJECT 07</span><span style="font-weight:400">60%</span></div>
    <div style="height:6px;margin:5px 0 0;border-radius:3px;background:var(--track)"><div style="width:60%;height:6px;border-radius:3px;background:#c8d9ee"></div></div>
  </div>
  <div class="badge"></div>
  <div class="footer-note">Home of the reef-keeper course<br>www.thecoralclinic.example</div>
  <div class="brand br">The Coral Clinic</div>
</section>

<section class="slide col-b" style="top:1446px">
  <h2 class="heading">Our Team</h2>
  <div class="photo" role="img" aria-label="Portrait photo of a team member" style="left:74px;top:65px;width:90px;height:90px;border-radius:50%;background:linear-gradient(180deg,#b9bcc2,#4d5058)"></div>
  <div class="photo" role="img" aria-label="Portrait photo of a team member" style="left:226px;top:65px;width:90px;height:90px;border-radius:50%;background:linear-gradient(180deg,#9a9da3,#3b3d43)"></div>
  <div class="photo" role="img" aria-label="Portrait photo of a team member" style="left:378px;top:65px;width:90px;height:90px;border-radius:50%;background:linear-gradient(180deg,#f1f1f2,#6b6d72)"></div>
  <div class="abs" style="left:44px;top:162px;width:150px;text-align:center">
    <div style="font-size:8px;font-weight:700;color:var(--yellow)">NAME</div>
    <div style="font-size:6.5px;letter-spacing:3px;margin-top:2px">DOCTOR</div>
    <p style="font-size:6.5px;line-height:12px;margin-top:9px">Lorem ipsum dolor sit amet, consectetuer adipiscing elit, sed diam nonummy nibh</p>
    <div style="display:flex;justify-content:center;gap:3px;margin-top:14px"><i style="width:9px;height:9px;border:1px solid #6f9bd6;border-radius:50%"></i><i style="width:9px;height:9px;border:1px solid #6f9bd6;border-radius:50%"></i><i style="width:9px;height:9px;border:1px solid #6f9bd6;border-radius:50%"></i></div>
  </div>
  <div class="abs" style="left:196px;top:162px;width:150px;text-align:center">
    <div style="font-size:8px;font-weight:700;color:var(--yellow)">NAME</div>
    <div style="font-size:6.5px;letter-spacing:3px;margin-top:2px">POTITION</div>
    <p style="font-size:6.5px;line-height:12px;margin-top:9px">Lorem ipsum dolor sit amet, consectetuer adipiscing elit, sed diam nonummy nibh</p>
    <div style="display:flex;justify-content:center;gap:3px;margin-top:14px"><i style="width:9px;height:9px;border:1px solid #6f9bd6;border-radius:50%"></i><i style="width:9px;height:9px;border:1px solid #6f9bd6;border-radius:50%"></i><i style="width:9px;height:9px;border:1px solid #6f9bd6;border-radius:50%"></i></div>
  </div>
  <div class="abs" style="left:348px;top:162px;width:150px;text-align:center">
    <div style="font-size:8px;font-weight:700;color:var(--yellow)">NAME</div>
    <div style="font-size:6.5px;letter-spacing:3px;margin-top:2px">POTITION</div>
    <p style="font-size:6.5px;line-height:12px;margin-top:9px">Lorem ipsum dolor sit amet, consectetuer adipiscing elit, sed diam nonummy nibh</p>
    <div style="display:flex;justify-content:center;gap:3px;margin-top:14px"><i style="width:9px;height:9px;border:1px solid #6f9bd6;border-radius:50%"></i><i style="width:9px;height:9px;border:1px solid #6f9bd6;border-radius:50%"></i><i style="width:9px;height:9px;border:1px solid #6f9bd6;border-radius:50%"></i></div>
  </div>
  <div class="badge"></div>
  <div class="footer-note">Home of the reef-keeper course<br>www.thecoralclinic.example</div>
  <div class="brand br">The Coral Clinic</div>
</section>

<!-- Row 6 -->
<section class="slide col-a" style="top:1797px">
  <div class="photo" role="img" aria-label="Photo of a red octopus on a black background" style="left:0;top:0;width:205px;height:305px;background:radial-gradient(ellipse at 70% 45%,#e0401c,#8a1a0c 45%,#120606 80%)"></div>
  <div class="abs" style="left:16px;top:258px;width:132px;height:30px;border-radius:8px;background:rgba(80,80,80,.85);font-size:8.5px;line-height:30px;padding-left:21px">Lorem ipsum name</div>
  <h2 class="heading" style="left:224px;top:76px">Picture with text</h2>
  <p class="body-text" style="left:224px;top:113px;width:286px">Lorem ipsum dolor sit amet, consectetuer adipiscing elit, sed diam nonummy nibh euismod tincidunt ut laoreet dolore magna aliquam erat volutpat. Ut wisi enim ad minim veniam, quis nostrud exerci tation ullamcorper suscipit lobortis nisl ut aliquip ex ea commodo consequat. Duis autem vel eum iriure dolor in hendrerit in vulputate velit esse molestie consequat, vel illum dolore eu feugiat nulla facilisis.</p>
  <div class="btn" style="left:224px;top:206px">MORE</div>
  <div class="brand br">The Coral Clinic</div>
</section>

<section class="slide col-b" style="top:1797px">
  <div class="photo" role="img" aria-label="Photo of a large shark swimming among fish in an aquarium" style="left:0;top:0;width:545px;height:305px;background:radial-gradient(ellipse at 45% 40%,#4c90b6,#1f5f93 45%,#0a2f5e 100%)"></div>
  <div class="brand" style="left:12px;top:27px">The Coral Clinic</div>
  <h2 class="abs" style="right:36px;top:214px;font-family:'Baloo 2',sans-serif;font-size:20px;line-height:20px;color:var(--yellow)">Section break</h2>
  <div class="abs" style="right:36px;top:241px;width:20px;height:2px;background:var(--yellow)"></div>
  <p class="abs" style="right:36px;top:259px;width:300px;text-align:right;font-size:6.2px;line-height:11px">Lorem ipsum dolor sit amet, consectetuer adipiscing elit, sed diam nonummy nibh euismod tincidunt ut laoreet dolore magna aliquam erat volutpat</p>
</section>

<!-- Row 7 -->
<section class="slide col-a" style="top:2149px">
  <h2 class="heading center">Map infographic</h2>
  <div class="photo" role="img" aria-label="World map with dotted travel routes and location pins" style="left:20px;top:58px;width:365px;height:217px;border-radius:40px;background:radial-gradient(ellipse at 50% 45%,rgba(180,205,235,.75),rgba(120,160,210,.35) 60%,rgba(60,110,190,0) 80%)"></div>
  <ul class="bullets" style="left:385px;top:84px">
    <li>Lorem Ipsum is simply dummy text of the printing and typesetting industry.</li>
    <li>Lorem Ipsum is simply dummy text of the printing and typesetting industry.</li>
  </ul>
  <div class="brand" style="left:420px;top:214px">The Coral Clinic</div>
</section>

<section class="slide col-b" style="top:2149px">
  <h2 class="heading">Any Questions ?</h2>
  <div class="laptop-screen" style="left:75px;top:85px;width:191px;height:126px"></div>
  <div class="photo" role="img" aria-label="X-ray image of a fish on the laptop screen" style="left:80px;top:90px;width:181px;height:121px;background:radial-gradient(ellipse at 45% 55%,#4a6f6a,#0c1414 60%,#000)"></div>
  <div class="laptop-base" style="left:53px;top:211px;width:235px"></div>
  <div class="abs" style="left:319px;top:81px;font-size:8px;font-weight:700">Follow The Coral Clinic on</div>
  <div class="abs" style="left:322px;top:102px;display:flex;gap:12px;font-size:8px;font-weight:600"><span>Reefbook</span><span>Shellgram</span></div>
  <div class="abs" style="left:322px;top:140px;font-size:7px;line-height:23px">
    <div style="display:flex;align-items:center;gap:14px"><svg width="12" height="12" viewBox="0 0 12 12"><path d="M2 1l3 0 1 3-2 1q1 3 3 3l1-2 3 1 0 3q-8 1-9-9z" fill="#fff"/></svg>+1 555 010 0199</div>
    <div style="display:flex;align-items:center;gap:14px"><svg width="12" height="12" viewBox="0 0 12 12" fill="none" stroke="#fff"><circle cx="6" cy="6" r="5"/><ellipse cx="6" cy="6" rx="2.2" ry="5"/><path d="M1 6h10"/></svg>www.coralclinic-site.example</div>
    <div style="display:flex;align-items:center;gap:14px"><svg width="12" height="12" viewBox="0 0 12 12"><rect x="0.5" y="2.5" width="11" height="7.5" fill="#fff"/><path d="M0.5 2.5l5.5 4 5.5-4" stroke="#0b3a8c" fill="none"/></svg>hello@coralclinic.example</div>
    <div style="display:flex;align-items:center;gap:14px"><svg width="12" height="12" viewBox="0 0 12 12"><path d="M6 11q-4-4.5-4-7a4 4 0 0 1 8 0q0 2.5-4 7z" fill="#fff"/><circle cx="6" cy="4" r="1.4" fill="#0b3a8c"/></svg>Add your location here</div>
  </div>
  <div class="badge"></div>
  <div class="footer-note">Home of the reef-keeper course<br>www.thecoralclinic.example</div>
  <div class="brand br">The Coral Clinic</div>
</section>

</body>
</html>
```